Brantley Advisory Group provides support for renewable energy projects to utilities and suppliers

I need a professional looking business card that is both simple and elegant and unique. My clients are mostly large organizations not individuals. I am a consultant with my own company that is small but would like to give clients the impression I am larger. Smart grid, fiber optics, software, field hardware, distribution automation, substation automation, operations, energy storage/batteries, microgrids, customer service, strategy/roadmaps, conservation, Automated Metering Infrastruture (AMI or smart meters) are all areas of focus.

Target Market(s)

Utilities, suppliers, governmental agencies involved in energy. All types of energy especially natural gas and electrical. Especially renewable energy or green projects.

Contact Information for Business Card

Name - Mark Brantley Cell Phone - 425.318.2746 Email - mbrantley@brantleyag-example.com
Company - Brantley Advisory Group (logo) Title - Principal

Font styles to use
Serif
Sans Serif

Colors

Designer to choose colors to be used in the design.

Requirements
Must have
• Simple and professional and powerful.
• Unique/creative design.
Nice to have
• Utilize color scheme to accent logo colors. Maybe some geometric pattern on edge of card with color.
Should not have
• Busy, complicated, traditional

```html
<!DOCTYPE html>
<html lang="en">
<head>
<meta charset="utf-8">
<title>Brantley Advisory Group – Business Card</title>
<link href="https://fonts.googleapis.com/css2?family=Ubuntu:wght@500;700&family=Lato:wght@300;400&display=swap" rel="stylesheet">
<style>
  :root {
    --page-bg: #d9dadc;
    --card-light: #f4f4f3;
    --card-dark: #232425;
    --brand-blue: #1e3fa0;
    --brand-green: #5e9a35;
    --brand-gray: #9a9b9d;
    --text-gray: #6a6b6d;
    --text-dark-mode: #3f5fb8;
  }
  * { box-sizing: border-box; margin: 0; padding: 0; }
  html, body {
    width: 1200px; height: 766px; overflow: hidden;
    background: var(--page-bg);
  }
  .canvas {
    width: 1200px; height: 766px;
    display: flex; align-items: center; justify-content: center; gap: 40px;
  }
  .card {
    position: relative;
    width: 540px; height: 309px;
    border-radius: 16px;
    overflow: hidden;
    box-shadow: 0 10px 28px rgba(0,0,0,.18);
  }
  .card--front { background: linear-gradient(180deg, #f9f9f8, var(--card-light)); }
  .card--back { background: var(--card-dark); }

  .edge-band {
    position: absolute; left: 0; right: 0; bottom: 0; height: 14px;
    display: flex;
  }
  .edge-band__blue { flex: 36; background: var(--brand-blue); }
  .edge-band__gray { flex: 34; background: var(--brand-gray); }
  .edge-band__green { flex: 30; background: var(--brand-green); }

  .brand {
    display: flex; align-items: center; gap: 16px;
    font-family: "Ubuntu", sans-serif; font-weight: 700;
    line-height: 1.02; letter-spacing: .5px;
  }
  .brand__mark { width: 46px; height: 46px; flex: none; border: 4px solid var(--brand-green); border-radius: 6px; }
  .brand__name { font-size: 34px; }

  .card--front .brand { position: absolute; left: 44px; top: 44px; color: var(--brand-blue); }
  .card--back .brand { position: absolute; left: 50%; top: 50%; transform: translate(-50%, -58%); color: var(--text-dark-mode); }
  .card--back .brand__name { font-size: 38px; }

  .person {
    position: absolute; left: 46px; top: 196px;
  }
  .person__name {
    font-family: "Lato", sans-serif; font-weight: 400;
    font-size: 22px; letter-spacing: .5px; color: var(--brand-blue); text-transform: uppercase;
  }
  .person__title {
    font-family: "Lato", sans-serif; font-weight: 300;
    font-size: 15px; color: var(--text-gray); margin-top: 2px; text-align: right;
  }
  .divider {
    position: absolute; left: 262px; top: 180px; width: 2px; height: 68px;
    background: var(--brand-green);
  }
  .contacts {
    position: absolute; left: 282px; top: 180px;
    list-style: none;
    font-family: "Lato", sans-serif; font-weight: 300; font-size: 13.5px; color: var(--text-gray);
  }
  .contacts li { display: flex; align-items: center; gap: 8px; height: 23px; }
  .contacts svg { width: 12px; height: 12px; flex: none; fill: var(--brand-blue); }
</style>
</head>
<body>
<main class="canvas">

  <article class="card card--front">
    <div class="brand">
      <span class="brand__mark"></span>
      <span class="brand__name">Brantley<br>Advisory Group</span>
    </div>

    <div class="person">
      <p class="person__name">Mark Brantley</p>
      <p class="person__title">Principal</p>
    </div>

    <span class="divider"></span>

    <ul class="contacts">
      <li>
        <svg viewBox="0 0 24 24" aria-hidden="true"><path d="M6.6 10.8a15.1 15.1 0 0 0 6.6 6.6l2.2-2.2a1 1 0 0 1 1-.25 11.4 11.4 0 0 0 3.6.6 1 1 0 0 1 1 1V20a1 1 0 0 1-1 1A17 17 0 0 1 3 4a1 1 0 0 1 1-1h3.5a1 1 0 0 1 1 1c0 1.25.2 2.45.6 3.6a1 1 0 0 1-.25 1z"/></svg>
        425.318.2746
      </li>
      <li>
        <svg viewBox="0 0 24 24" aria-hidden="true"><path d="M2 5h20v14H2z M3.5 6.5 12 13l8.5-6.5" fill="var(--brand-blue)" stroke="#fff" stroke-width="1.6"/></svg>
        mbrantley@brantleyag-example.com
      </li>
      <li>
        <svg viewBox="0 0 24 24" aria-hidden="true"><circle cx="12" cy="12" r="10"/><path d="M2 12h20M12 2c3 3 3 17 0 20M12 2c-3 3-3 17 0 20M4 7h16M4 17h16" stroke="#fff" stroke-width="1.3" fill="none"/></svg>
        www.brantleyag-example.com
      </li>
    </ul>

    <div class="edge-band">
      <span class="edge-band__blue"></span>
      <span class="edge-band__gray"></span>
      <span class="edge-band__green"></span>
    </div>
  </article>

  <article class="card card--back">
    <div class="brand">
      <span class="brand__mark"></span>
      <span class="brand__name">Brantley<br>Advisory Group</span>
    </div>

    <div class="edge-band">
      <span class="edge-band__blue"></span>
      <span class="edge-band__gray"></span>
      <span class="edge-band__green"></span>
    </div>
  </article>

</main>
</body>
</html>
```